Desktop and Networking Support Course 9.17.25

Important the ad should not be very busy with the text taking up the major part of the ad .. please do not make the text so big that it takes up most of the ad..
Flyer Design Brief for Graphic Artist
also i am looking for something unique or creative that it will stand out .
Size & Layout:
Full Page with Bleed: 8” x 10.75” + 0.25” bleed on all sides.
Footer Space: Leave a 1-inch margin at the bottom for footer content (e.g., contact info, logo, or call-to-action).
Target Audience:
College-age students (around 24 years old)
Located in the USA
Interested in creative, professional, and career-building opportunities
Purpose:
To attract students to enroll in a college program
Flyer should be eye-catching, unique, and creative
Text must be clear and readable,
Design Style:
Use vector art, typography, or photography — your choice
If using photography, feature a white young professional USA citizen:
Wearing a white collared shirt
not with long hair
Creative Direction:
The flyer should stand out visually — something people would want to look at and keep
Showcase creativity and professionalism
Use bold colors, dynamic layout, or unexpected design elements to grab attention
Avoid clutter — keep the design balanced and clean
Text Suggestions (can be adjusted):
Footer,
please leave one inch on the bottom for the footer

```html
<!DOCTYPE html>
<html lang="en">
<head>
<meta charset="utf-8">
<title>Desktop &amp; Network Support Course</title>
<link rel="stylesheet" href="https://fonts.googleapis.com/css2?family=Roboto:wght@700;900&family=Open+Sans:ital,wght@0,400;0,600;0,700;1,400&display=swap">
<style>
  :root {
    --navy: #0b2784;
    --gold: #c2a41f;
    --blue: #054192;
    --icon: #0a3d95;
    --ink: #111111;
    --white: #ffffff;
  }
  * { margin: 0; padding: 0; box-sizing: border-box; }
  html, body { width: 873px; height: 1200px; overflow: hidden; background: var(--white); }
  .flyer { position: relative; width: 873px; height: 1200px; overflow: hidden; background: var(--white); font-family: "Open Sans", sans-serif; color: var(--ink); }

  .headline { position: absolute; left: 0; width: 873px; top: 66px; text-align: center; font-family: "Roboto", sans-serif; font-weight: 900; line-height: 60px; letter-spacing: 0.5px; }
  .headline .line-top { display: block; color: var(--navy); font-size: 58px; }
  .headline .line-bottom { display: block; color: var(--gold); font-size: 58px; }

  .course-title { position: absolute; left: 0; width: 873px; top: 199px; text-align: center; font-family: "Roboto", sans-serif; font-weight: 700; font-size: 22px; letter-spacing: 0.3px; }

  .hero-art { position: absolute; left: 44px; top: 240px; width: 608px; height: 408px; border-radius: 6px;
    background: radial-gradient(ellipse at 62% 45%, #dcd9ec 0%, #ecebf4 45%, #f8f8fc 75%, #ffffff 100%); }

  .stat { position: absolute; top: 655px; height: 104px; background: var(--blue); color: var(--white); }
  .stat-left { left: 50px; width: 349px; }
  .stat-right { left: 456px; width: 372px; }
  .stat .badge { position: absolute; left: 27px; top: 23px; width: 58px; height: 58px; border-radius: 50%; background: var(--white); display: flex; align-items: center; justify-content: center; }
  .stat .copy { position: absolute; left: 108px; top: 10px; }
  .stat-right .copy { left: 101px; }
  .stat .big { font-weight: 700; font-size: 23px; line-height: 28px; display: block; }
  .stat .small { font-size: 18px; line-height: 28px; display: block; }
  .stat .source { font-style: italic; font-size: 16px; line-height: 30px; display: block; }

  .feature { position: absolute; display: flex; align-items: center; }
  .feature .ring { width: 62px; height: 62px; border-radius: 50%; border: 2.5px solid var(--gold); display: flex; align-items: center; justify-content: center; flex: none; }
  .feature .label { margin-left: 20px; font-size: 18.5px; line-height: 30px; }
  .f1 { left: 75px; top: 793px; }
  .f2 { left: 473px; top: 793px; }
  .f3 { left: 75px; top: 884px; }
  .f4 { left: 473px; top: 884px; }

  .offer { position: absolute; left: 0; width: 873px; top: 972px; text-align: center; font-family: "Roboto", sans-serif; font-weight: 700; font-size: 26.5px; }

  .footer { position: absolute; left: 0; top: 1033px; width: 873px; height: 167px; background: var(--blue); }
  .footer .cta { position: absolute; left: 0; width: 873px; top: 18px; text-align: center; color: var(--white); font-family: "Roboto", sans-serif; font-weight: 700; font-size: 31px; }
</style>
</head>
<body>
<div class="flyer">
  <h1 class="headline">
    <span class="line-top">YOUR CAREER IS</span>
    <span class="line-bottom">JUST A CLICK AWAY</span>
  </h1>
  <p class="course-title">DESKTOP &amp; NETWORK SUPPORT COURSE</p>

  <div class="hero-art" role="img" aria-label="Vector illustration of a young professional in a suit working at a laptop, surrounded by office and technology icons, with a winding career path from a briefcase"></div>

  <div class="stat stat-left">
    <div class="badge">
      <svg width="32" height="36" viewBox="0 0 32 36" fill="var(--icon)">
        <circle cx="16" cy="9" r="6" fill="none" stroke="var(--icon)" stroke-width="2.5"/>
        <path d="M7 24c0-5 4-8 9-8s9 3 9 8z"/>
        <path d="M5 26l1.2 2.6 2.8.3-2.1 1.9.6 2.8L5 32.2 2.5 33.6l.6-2.8L1 28.9l2.8-.3z"/>
        <path d="M16 26l1.2 2.6 2.8.3-2.1 1.9.6 2.8L16 32.2l-2.5 1.4.6-2.8-2.1-1.9 2.8-.3z"/>
        <path d="M27 26l1.2 2.6 2.8.3-2.1 1.9.6 2.8L27 32.2l-2.5 1.4.6-2.8-2.1-1.9 2.8-.3z"/>
      </svg>
    </div>
    <div class="copy">
      <span class="big">90%</span>
      <span class="big">Employment Rate</span>
      <span class="small">Class of 2024</span>
    </div>
  </div>

  <div class="stat stat-right">
    <div class="badge">
      <svg width="32" height="34" viewBox="0 0 32 34" fill="var(--icon)">
        <rect x="3" y="2" width="26" height="15" rx="1.5" fill="none" stroke="var(--icon)" stroke-width="2"/>
        <path d="M11 7l-3 2.5 3 2.5M21 7l3 2.5-3 2.5M17.5 6l-3 7" fill="none" stroke="var(--icon)" stroke-width="1.6"/>
        <circle cx="16" cy="21" r="4.5"/>
        <path d="M7 33c0-5 4-7 9-7s9 2 9 7z"/>
      </svg>
    </div>
    <div class="copy">
      <span class="big">Prepare for 3 of the</span>
      <span class="big">Top 10 Tech Jobs</span>
      <span class="source">National Career Review 2025</span>
    </div>
  </div>

  <div class="feature f1">
    <div class="ring">
      <svg width="30" height="28" viewBox="0 0 30 28" fill="var(--icon)">
        <rect x="1" y="1" width="28" height="19" rx="2"/>
        <rect x="11" y="20" width="8" height="4"/>
        <rect x="7" y="24" width="16" height="2.5" rx="1"/>
        <circle cx="14" cy="12" r="4" fill="none" stroke="var(--white)" stroke-width="1.8"/>
        <circle cx="23" cy="6" r="1.6" fill="var(--white)"/>
      </svg>
    </div>
    <div class="label">Master Vantix<br>Operating Systems</div>
  </div>

  <div class="feature f2">
    <div class="ring">
      <svg width="30" height="32" viewBox="0 0 30 32" fill="var(--icon)">
        <path d="M15 1L1 7l14 6 14-6z"/>
        <path d="M6 10v5h18v-5l-9 4z"/>
        <circle cx="15" cy="23" r="8" fill="none" stroke="var(--icon)" stroke-width="2.2"/>
        <path d="M7 23h16M15 15c-4 4-4 12 0 16M15 15c4 4 4 12 0 16" fill="none" stroke="var(--icon)" stroke-width="1.6"/>
      </svg>
    </div>
    <div class="label">Hands-On Desktop &amp;<br>Network Training</div>
  </div>

  <div class="feature f3">
    <div class="ring">
      <svg width="32" height="34" viewBox="0 0 32 34" fill="var(--icon)">
        <path d="M15 4a9 9 0 0 0-6 15.5V24h12v-4.5A9 9 0 0 0 15 4z"/>
        <rect x="10" y="26" width="10" height="2" rx="1"/>
        <rect x="11" y="30" width="8" height="2" rx="1"/>
        <path d="M15 6v17" stroke="var(--white)" stroke-width="1.5"/>
        <path d="M25 6l3-3M27 13h4M15 0v2" stroke="var(--icon)" stroke-width="1.6"/>
      </svg>
    </div>
    <div class="label">Real-World<br>Troubleshooting Skills</div>
  </div>

  <div class="feature f4">
    <div class="ring">
      <svg width="32" height="32" viewBox="0 0 32 32" fill="var(--icon)">
        <path d="M13 2h6l1 4 3 1.5 3.5-2 4 4-2 3.5L30 16l-1.5 3 2 3.5-4 4-3.5-2L20 26l-1 4h-6l-1-4-3-1.5-3.5 2-4-4 2-3.5L2 16l1.5-3-2-3.5 4-4 3.5 2L12 6z"/>
        <circle cx="13" cy="14" r="3.2" fill="var(--white)"/>
        <path d="M7 23c0-4 3-5.5 6-5.5s6 1.5 6 5.5z" fill="var(--white)"/>
        <circle cx="25" cy="7" r="5" fill="var(--icon)" stroke="var(--white)" stroke-width="1.2"/>
        <path d="M22.6 7l1.7 1.7 3-3" fill="none" stroke="var(--white)" stroke-width="1.5"/>
      </svg>
    </div>
    <div class="label">Ready for IT Jobs</div>
  </div>

  <p class="offer">In-Person and Remote Options Partial Scholarships Offered</p>

  <footer class="footer">
    <p class="cta">CONTACT US</p>
  </footer>
</div>
</body>
</html>
```